Biz Card Design TPVC

New business card for a new company.
Logo was completed by a designer on ArtFlock and looking to continue requesting additional services.
Company Name: Tidal Prime Voltage Collective
Although this company is starting in Canada, we will be moving towards a global presence within the next 6 months.
Key elements to this business are as follows.
Energy Procurement
Energy Reduction Services
Demand Side Consulting
Energy Efficiency Consulting
Saving Clients Money
Helping Them Go "Green"
Managing Their Energy Requirements
Basically the goal for our company is to find the best procurement solution for our clients and reduce their energy consumption. This reduces their expenses and the amount of greenhouse gas they produce on a daily basis.
I have been in the energy footprint for the last 20 years and know that most companies are looking to "do whatever is necessary to get them to sign on the dotted line". I would prefer to walk away from a client that I can't help than to put them into a situation that they will regret for years to come. This is where the "TIDAL" part of the company name comes from.
The following is a catch phrase that encompasses what we do.
"Reducing your carbon footprint & energy bill at the same time!"
The back of the card needs to have this statement along with some sort of illustration. The back is a playground for creative ideas.
The front of the card needs the following.
Logo.
First & Last Name (Gus Marwick)
Title (Energy Warrior)
Phone Number (555) 314-2768
Fax Number (555) 862-4091
Email Address gus@tidalprimevoltage.example
Address 47 Orchard Lane Toronto Ontario K4P 2Z7
I want it to be a card that is remembered when any of my staff give it to a customer. It HAS to stand out.
Target Market(s)
Business Owners, Decision Makers, 30 to 65+
Industry/Entity Type
Business
Look and feel
Each slider illustrates characteristics of the customer's brand and the style your logo design should communicate.

```html
<!DOCTYPE html>
<html lang="en">
<head>
<meta charset="utf-8">
<title>Tidal Prime Voltage Collective – Business Card</title>
<link href="https://fonts.googleapis.com/css2?family=Nunito:wght@800&family=Signika:wght@600&family=Open+Sans:wght@400&family=Questrial&display=swap" rel="stylesheet">
<style>
  :root {
    --green: #22a84a;
    --green-deep: #0f8a3c;
    --green-light: #c9e08f;
    --blue: #3f6fb8;
    --blue-bright: #1a8fd0;
    --ink: #1a1a1a;
    --paper: #ffffff;
  }
  html, body {
    margin: 0;
    padding: 0;
    overflow: hidden;
    background: var(--paper);
  }
  .card {
    position: relative;
    width: 1200px;
    height: 686px;
    background: var(--paper);
    overflow: hidden;
  }
  .card__art {
    position: absolute;
    left: 0;
    top: 0;
    width: 1200px;
    height: 686px;
  }
  .brand {
    position: absolute;
    left: 560px;
    top: 80px;
    width: 626px;
    text-align: center;
  }
  .brand__dot {
    display: block;
    width: 74px;
    height: 74px;
    margin: 0 auto 22px;
    border-radius: 50%;
    background: var(--green);
  }
  .brand__name {
    margin: 0;
    font-family: "Nunito", sans-serif;
    font-weight: 800;
    font-size: 31px;
    color: var(--blue);
    letter-spacing: 0.2px;
    white-space: nowrap;
  }
  .person {
    position: absolute;
    left: 600px;
    top: 348px;
    width: 578px;
    text-align: center;
  }
  .person__name {
    margin: 0;
    font-family: "Signika", sans-serif;
    font-weight: 600;
    font-size: 41px;
    line-height: 1.1;
    letter-spacing: 0.5px;
  }
  .person__first { color: var(--green); }
  .person__last { color: var(--blue); }
  .person__title {
    margin: 2px 0 0;
    font-family: "Open Sans", sans-serif;
    font-size: 23px;
    letter-spacing: 1.2px;
    color: var(--ink);
  }
  .contact {
    position: absolute;
    left: 600px;
    top: 510px;
    width: 578px;
    margin: 0;
    text-align: center;
    font-family: "Questrial", sans-serif;
    font-size: 25px;
    line-height: 34px;
    color: var(--ink);
    font-style: normal;
  }
  .contact__label { color: var(--blue); }
</style>
</head>
<body>
  <main class="card">
    <svg class="card__art" viewBox="0 0 1200 686" aria-hidden="false">
      <defs>
        <linearGradient id="sweepGradient" x1="0" y1="0" x2="1" y2="1">
          <stop offset="0" stop-color="#0f8a3c"/>
          <stop offset="0.45" stop-color="#7cbf5a"/>
          <stop offset="0.75" stop-color="#c9e08f"/>
          <stop offset="1" stop-color="#1a8fd0"/>
        </linearGradient>
      </defs>
      <path role="img" aria-label="Decorative sweep of green leaf shapes with a blue swoosh"
            d="M0,0 H415 C505,150 525,380 330,560 C470,540 590,600 640,686 H0 Z"
            fill="url(#sweepGradient)"/>
    </svg>

    <header class="brand">
      <span class="brand__dot" aria-hidden="true"></span>
      <h1 class="brand__name">Tidal Prime Voltage Collective</h1>
    </header>

    <section class="person">
      <h2 class="person__name"><span class="person__first">Gus</span> <span class="person__last">Marwick</span></h2>
      <p class="person__title">Energy Warrior</p>
    </section>

    <address class="contact">
      47 Orchard Lane Toronto Ontario K4P 2Z7<br>
      <span class="contact__label">Ph:</span> (555) 314-2768<br>
      <span class="contact__label">Fax:</span> (555) 862-4091<br>
      <span class="contact__label">Email:</span> gus@tidalprimevoltage.example
    </address>
  </main>
</body>
</html>
```